Website Design For our Tour Company

We need a face lift on our current website. I want it to look the best! Lots of videos. An easy to use website to obtain easy conversions. I want people to feel like they are on the tour just by looking at our website. My current website is just bland and unprofessional looking. I want it to be incredibly mobile friendly and look great on the desk top. Our current website is https://www.kellbrookvoyages.example/
I would like there to be an option where the viewer can select what language they would like to read in. Im hoping you can pull a-lot of media and videos from out facebook page. Im not happy with most of my descriptions for the product and tours we offer. Looking for professional help.

Our two main activities are Summer and Winter Tours
In The Summer the main things we do our Jet Boat & Jet Ski Tours.

In The Winter our main tour is luxury first class Aurora Viewing. I Would like to see a-lot of aurora video/photos as I believe that gets peoples attention!

Target Market(s)

Travelers from china and around the world

Coding

Coded - Design and coding required

Number of Pages Required

5+ page

Requirements
Must have
• be able to select what when language you would like to read the website in.
Nice to have
• The overall look and feel I want for the website is luxury, fancy, royalty. Think Gerald Mossworth. I like the Luxury gold colors. I need the website to look ridiculously professional

incorporate Lots of Aurora photos / videos as one of our main tours is Aurora

```html
<!DOCTYPE html>
<html lang="en">
<head>
<meta charset="utf-8">
<title>Kellbrook Premier Tours</title>
<link href="https://fonts.googleapis.com/css2?family=Kanit:wght@500;600;700&family=Open+Sans:wght@400;600&display=swap" rel="stylesheet">
<style>
:root{
  --gold:#b8952a;
  --ink:#1d1d1d;
  --text:#3a3a3a;
  --white:#ffffff;
  --faint:#e6e6e6;
  --teal-dark:#1e3a44;
  --footer:#1b272b;
  --hero-b:#c9913e;
  --aurora:#3fbf8a;
}
*{box-sizing:border-box;margin:0;padding:0}
html,body{width:1200px;height:4501px;overflow:hidden;background:var(--white)}
body{position:relative;font-family:"Open Sans",Arial,sans-serif;color:var(--text)}
.abs{position:absolute}

/* Hero */
.hero{left:0;top:0;width:1200px;height:700px;background:linear-gradient(180deg,#4a4f5c 0%,#8a6a45 40%,var(--hero-b) 52%,#6f6a70 70%,#3e4552 100%)}
.brand{left:175px;top:30px;display:flex;align-items:center;gap:10px;color:var(--white)}
.brand-dot{width:52px;height:52px;border-radius:50%;border:2px solid var(--white)}
.brand-name{font-family:"Kanit",sans-serif;font-weight:500;font-size:24px;letter-spacing:2px;line-height:1}
.contact-chip{display:flex;align-items:center;gap:10px;color:var(--white);top:44px}
.chip-icon{width:32px;height:32px;border-radius:50%;background:var(--gold);display:flex;align-items:center;justify-content:center}
.chip-label{display:block;font-size:10px;line-height:1.3}
.chip-value{font-size:13px}
.nav{left:143px;top:129px;width:914px;height:47px;background:var(--white);display:flex;align-items:center}
.nav ul{list-style:none;display:flex;margin-left:38px;font-size:10.5px;color:var(--ink)}
.nav li{margin-right:46px}
.nav .tools{position:absolute;left:690px;display:flex;align-items:center;gap:12px}
.lang{display:flex;align-items:center;gap:4px;font-size:10.5px;color:var(--ink);border:1px solid #cfcfcf;border-radius:10px;padding:2px 7px}
.book{left:938px;top:129px;width:119px;height:47px;background:var(--gold);color:var(--white);font-size:12px;display:flex;align-items:center;justify-content:center}
.hero-title{left:0;width:1200px;top:272px;text-align:center;color:var(--white);font-family:"Kanit",sans-serif;font-weight:600;font-size:70px;letter-spacing:1px;line-height:1.2}
.hero-sub{left:0;width:1200px;top:375px;text-align:center;color:var(--white);font-size:11.5px}
.btn{background:var(--gold);color:var(--white);border-radius:20px;display:flex;align-items:center;justify-content:center;font-size:11px}
.thumb{left:963px;width:64px;height:64px;border:2px solid var(--white);display:flex;align-items:center;justify-content:center}
.play{width:22px;height:22px;border-radius:50%;background:rgba(0,0,0,.35);display:flex;align-items:center;justify-content:center}

/* Section headings */
.sec-title{left:0;width:1200px;text-align:center;font-family:"Kanit",sans-serif;font-weight:600;font-size:38px;color:var(--ink);line-height:1.2}
.ghost{font-family:"Kanit",sans-serif;font-weight:700;color:var(--faint);white-space:nowrap}
.ornament{left:475px;width:250px;height:30px}

/* About */
.about-title{left:154px;top:790px;font-family:"Kanit",sans-serif;font-weight:600;font-size:29px;color:var(--ink);line-height:1.2}
.about-bar{left:154px;top:859px;width:82px;height:4px;background:var(--gold)}
.about-list{left:154px;top:890px;width:455px;list-style:none;font-size:10.5px;line-height:27px}
.about-list li{position:relative;padding-left:13px;margin-bottom:26px}
.about-list li::before{content:"\2714";position:absolute;left:0;top:0;color:var(--gold);font-size:9px}
.emblem{left:660px;top:800px;width:330px;height:300px;display:flex;flex-direction:column;align-items:center;justify-content:center;gap:16px}
.emblem-circle{width:180px;height:180px;border-radius:50%;background:#3d2f63}
.emblem-name{font-family:"Kanit",sans-serif;font-weight:600;font-size:26px;color:#3d2f63;letter-spacing:1px}
.vert{writing-mode:vertical-rl;transform:rotate(180deg)}

/* Resort */
.resort-bg{left:0;top:1230px;width:1200px;height:770px;background:linear-gradient(180deg,#3e5458 0%,var(--teal-dark) 55%,#0f2630 100%)}
.resort-card{left:141px;top:1350px;width:341px;height:547px;background:var(--white)}
.resort-title{left:234px;top:1412px;font-family:"Kanit",sans-serif;font-weight:600;font-size:30px;color:var(--ink);line-height:1.2}
.resort-sub{left:234px;top:1462px;font-size:10.5px}
.resort-body{left:165px;top:1544px;width:300px;text-align:center;font-size:11px;line-height:27.4px}

/* Car */
.car{left:143px;top:2208px;width:444px;height:392px;background:linear-gradient(180deg,#c9d2d8 0%,#e8ecef 45%,#b9bcbf 100%)}
.car-text{left:606px;top:2248px;width:440px;font-size:11px;line-height:30.6px}

/* Gallery */
.cell{width:300px;height:259px}
.g-title{left:333px;top:2875px;font-family:"Kanit",sans-serif;font-weight:600;font-size:21px;color:var(--white);line-height:1.2}
.g-text{left:333px;top:2920px;width:240px;font-size:11px;line-height:24px;color:#d8d8d8}

/* Blog */
.blog-card{width:292px;height:208px;top:3553px;overflow:hidden;box-shadow:0 2px 8px rgba(0,0,0,.15)}
.blog-img{position:absolute;inset:0}
.blog-cut{position:absolute;inset:0;background:var(--white);clip-path:polygon(100% 0,100% 100%,55% 100%)}
.diamond{position:absolute;width:48px;height:48px;background:var(--gold);transform:rotate(45deg);left:204px;top:52px;display:flex;align-items:center;justify-content:center}
.date{position:absolute;left:218px;top:124px;width:40px;text-align:center;font-size:12px;line-height:22px;color:var(--ink)}
.blog-title{width:292px;top:3782px;font-family:"Kanit",sans-serif;font-weight:600;font-size:19px;line-height:31px;color:var(--ink);padding-left:18px}

/* Footer */
.footer{left:0;top:3870px;width:1200px;height:631px;background:linear-gradient(180deg,#22333a 0%,var(--footer) 60%,#141d20 100%)}
.foot-h{top:4020px;font-family:"Kanit",sans-serif;font-weight:500;font-size:22px;color:var(--white);line-height:1.2}
.field{background:var(--white);border-radius:14px;font-size:10px;color:#9a9a9a;padding:10px 18px}
.submit{left:542px;top:4339px;width:127px;height:44px;background:var(--white);border-radius:22px;display:flex;align-items:center;justify-content:center;font-weight:600;font-size:15px;color:var(--ink)}
.info{left:724px;display:flex;align-items:center;gap:14px;font-size:11px;color:var(--white)}
.info-icon{width:32px;height:32px;border-radius:50%;border:1px solid var(--white);display:flex;align-items:center;justify-content:center}
.rule{left:143px;top:4432px;width:914px;height:1px;background:rgba(255,255,255,.4)}
.copy{left:0;width:1200px;top:4457px;text-align:center;font-size:10px;color:var(--white)}
</style>
</head>
<body>

<!-- HERO -->
<div class="abs hero" role="img" aria-label="Video banner: winter sunset over a snowy river with birch trees and a mug in the foreground"></div>
<div class="abs brand">
  <span class="brand-dot"></span>
  <span class="brand-name">KELLBROOK VOYAGES</span>
</div>
<div class="abs contact-chip" style="left:626px">
  <span class="chip-icon"><svg width="14" height="14" viewBox="0 0 24 24"><path fill="#fff" d="M6.6 10.8a15 15 0 0 0 6.6 6.6l2.2-2.2c.3-.3.7-.4 1-.2 1.1.4 2.3.6 3.6.6.6 0 1 .4 1 1V20c0 .6-.4 1-1 1A17 17 0 0 1 3 4c0-.6.4-1 1-1h3.5c.6 0 1 .4 1 1 0 1.3.2 2.5.6 3.6.1.3 0 .7-.2 1z"/></svg></span>
  <span><span class="chip-label">Support Call</span><span class="chip-value">555-014-2290</span></span>
</div>
<div class="abs contact-chip" style="left:802px">
  <span class="chip-icon"><svg width="14" height="14" viewBox="0 0 24 24"><path fill="#fff" d="M12 2a7 7 0 0 0-7 7c0 5 7 13 7 13s7-8 7-13a7 7 0 0 0-7-7zm0 9.5A2.5 2.5 0 1 1 12 6.5a2.5 2.5 0 0 1 0 5z"/></svg></span>
  <span><span class="chip-label">Location</span><span class="chip-value">123 Lorem ipsum State Park</span></span>
</div>
<nav class="abs nav">
  <ul>
    <li>HOME</li><li>ABOUT US</li><li>SUMMER</li><li>WINTER</li><li>BLOG</li><li>CAR RENTAL</li><li>CONTACT US</li>
  </ul>
  <div class="tools">
    <span class="lang" aria-label="Select language">
      <svg width="11" height="11" viewBox="0 0 24 24"><circle cx="12" cy="12" r="9" fill="none" stroke="#1d1d1d" stroke-width="2"/><path d="M3 12h18M12 3c3 3 3 15 0 18M12 3c-3 3-3 15 0 18" fill="none" stroke="#1d1d1d" stroke-width="1.5"/></svg>
      EN
      <svg width="7" height="7" viewBox="0 0 10 10"><path d="M1 3l4 4 4-4" fill="none" stroke="#1d1d1d" stroke-width="1.5"/></svg>
    </span>
    <svg width="16" height="16" viewBox="0 0 24 24"><circle cx="12" cy="7" r="4.5" fill="#1d1d1d"/><path d="M3 22c0-5 4-8 9-8s9 3 9 8z" fill="#1d1d1d"/></svg>
    <svg width="16" height="16" viewBox="0 0 24 24"><circle cx="10" cy="10" r="7" fill="none" stroke="#1d1d1d" stroke-width="2"/><path d="M15 15l6 6" stroke="#1d1d1d" stroke-width="2"/></svg>
  </div>
</nav>
<div class="abs book">BOOK NOW</div>
<h1 class="abs hero-title">Kellbrook Premier</h1>
<p class="abs hero-sub">Integer accumsan, purus vitae euismod volutpat, erat nisl molestie urna, et convallis nisi nisi at massa.</p>
<div class="abs btn" style="left:533px;top:423px;width:133px;height:36px">Find Out More</div>
<div class="abs thumb" style="top:246px;background:linear-gradient(180deg,#16324a,var(--aurora) 55%,#0d1a26)" role="img" aria-label="Aurora viewing video thumbnail: green northern lights over a winter night sky">
  <span class="play"><svg width="10" height="10" viewBox="0 0 10 10"><path d="M2 1l7 4-7 4z" fill="#fff"/></svg></span>
</div>
<div class="abs thumb" style="top:330px;background:linear-gradient(180deg,#6ea3c8,#2a5e86)" role="img" aria-label="Video thumbnail: kayaker on a lake">
  <span class="play"><svg width="10" height="10" viewBox="0 0 10 10"><path d="M2 1l7 4-7 4z" fill="#fff"/></svg></span>
</div>
<div class="abs thumb" style="top:412px;background:linear-gradient(180deg,#4f7a3a,#c8862a)" role="img" aria-label="Video thumbnail: kayak on a forest river">
  <span class="play"><svg width="10" height="10" viewBox="0 0 10 10"><path d="M2 1l7 4-7 4z" fill="#fff"/></svg></span>
</div>
<svg class="abs" style="left:0;top:600px" width="1200" height="102" viewBox="0 0 1200 102">
  <polygon points="0,100 928,18 1200,90 1200,102 0,102" fill="#fff"/>
  <polyline points="440,52 928,14 1110,80" fill="none" stroke="#b8952a" stroke-width="4"/>
  <circle cx="928" cy="24" r="13" fill="#fff" stroke="#b8952a" stroke-width="2"/>
</svg>

<!-- ABOUT -->
<h2 class="abs about-title">Welcome To Kellbrook Premier Tour</h2>
<div class="abs about-bar"></div>
<ul class="abs about-list">
  <li>Owen - Life-long Alaskan - Local expert, loves the outdoors, construction, &amp; adventures</li>
  <li>Rhys - Life-long Alaskan - Local expert entrepreneur, loves Alaska, always ready for an<br>adventure and a fun time!</li>
  <li>Elena - Life-long Alaska - Local expert, company cook, organizes the activities &amp; schedule.<br>Without her we have no organization.</li>
</ul>
<div class="abs btn" style="left:147px;top:1109px;width:99px;height:39px">Read More</div>
<div class="abs emblem">
  <span class="emblem-circle"></span>
  <span class="emblem-name">KELLBROOK VOYAGES</span>
</div>
<div class="abs ghost vert" style="left:1040px;top:742px;font-size:78px;line-height:1">ABOUT US</div>

<!-- RESORT -->
<div class="abs resort-bg" role="img" aria-label="Dusky lake with dark spruce forest and a kayak bow"></div>
<svg class="abs" style="left:0;top:1210px" width="1200" height="90" viewBox="0 0 1200 90">
  <polygon points="0,0 1200,0 1200,14 620,74 0,14" fill="#fff"/>
  <polyline points="0,10 620,70 1200,10" fill="none" stroke="#b8952a" stroke-width="6"/>
</svg>
<svg class="abs" style="left:0;top:1930px" width="1200" height="90" viewBox="0 0 1200 90">
  <polygon points="0,80 620,14 1200,80 1200,90 0,90" fill="#fff"/>
  <polyline points="0,78 620,12 1200,78" fill="none" stroke="#b8952a" stroke-width="6"/>
</svg>
<div class="abs resort-card"></div>
<div class="abs ghost vert" style="left:150px;top:1400px;font-size:48px;line-height:1;color:#ececec">TRAVEL RESORT</div>
<h2 class="abs resort-title">Resort LLC</h2>
<p class="abs resort-sub">The Only Travel Agency for You</p>
<svg class="abs" style="left:234px;top:1492px" width="160" height="24" viewBox="0 0 160 24"><line x1="0" y1="12" x2="62" y2="12" stroke="#b8952a"/><circle cx="80" cy="12" r="10" fill="none" stroke="#b8952a" stroke-width="1.5"/><line x1="98" y1="12" x2="160" y2="12" stroke="#b8952a"/></svg>
<p class="abs resort-body">Kellbrook Resorts, LLC specializes in providing the best travel services in Fairbanks, Alaska. We've been in Fairbanks since 1995, creating customized itineraries for our clients based around their personal plans and preferences. In our line of work we don't only make plans, we help you build experiences and memories. Let us arrange the details of your next trip — call today for a free consultation.</p>
<div class="abs btn" style="left:262px;top:1789px;width:100px;height:37px">View All</div>
<div class="abs" style="left:505px;top:1350px;width:264px;height:261px;background:linear-gradient(170deg,#7f8c92,#3e4b3e 70%,#c3b23a)" role="img" aria-label="Riders on a jet ski at a dock"></div>
<div class="abs" style="left:791px;top:1350px;width:264px;height:261px;background:linear-gradient(180deg,#6d8294,#2f4a4e 60%,#4a5860)" role="img" aria-label="Two riders on a jet ski on a lake"></div>
<div class="abs" style="left:505px;top:1637px;width:264px;height:261px;background:linear-gradient(180deg,#8a93a8,#3a3f55)" role="img" aria-label="Person holding a fish while ice fishing"></div>
<div class="abs" style="left:791px;top:1637px;width:264px;height:261px;background:linear-gradient(180deg,#a2a8bb,#5a5f73)" role="img" aria-label="Two people ice fishing on a frozen lake"></div>

<!-- CAR RENTAL -->
<div class="abs ghost" style="left:452px;top:2010px;font-size:100px;line-height:1">Rental</div>
<h2 class="abs sec-title" style="top:2050px">Car Rental</h2>
<svg class="abs ornament" style="top:2114px" viewBox="0 0 250 30"><line x1="0" y1="15" x2="100" y2="15" stroke="#999"/><circle cx="125" cy="15" r="12" fill="none" stroke="#b8952a" stroke-width="1.5"/><line x1="150" y1="15" x2="250" y2="15" stroke="#999"/></svg>
<div class="abs car" role="img" aria-label="White SUV parked by the waterfront"></div>
<p class="abs car-text">Vivamus convallis ac tellus eu finibus. Donec vel augue nisi. Praesent egestas arcu vitae orci commodo rhoncus. Suspendisse vitae enim eget magna feugiat luctus in eu erat. Vestibulum gravida mi in neque vehicula, nec tincidunt risus laoreet. Donec in nulla fringilla, dignissim mauris eu, consectetur mauris. Nullam vestibulum purus tempor, luctus ante id, iaculis odio. Nullam tempus purus consequat magna tristique fringilla. Nunc rhoncus ipsum mauris, in hendrerit sem sollicitudin ac. Pellentesque eget fringilla nisi, vitae tincidunt justo. Phasellus luctus ornare turpis, quis semper ex egestas non. Phasellus et tempus velit, molestie lacinia metus. Curabitur fermentum luctus arcu, non maximus justo imperdiet nec. Vestibulum iaculis viverra purus, a mollis odio pellentesque vitae. Lorem ipsum dolor sit amet, consectetur adipiscing elit.</p>

<!-- GALLERY -->
<div class="abs ghost" style="left:734px;top:2686px;font-size:104px;line-height:1">Our Gallery</div>
<h2 class="abs sec-title" style="top:2678px">Photography</h2>
<svg class="abs ornament" style="top:2742px" viewBox="0 0 250 30"><line x1="0" y1="15" x2="100" y2="15" stroke="#999"/><circle cx="125" cy="15" r="12" fill="none" stroke="#b8952a" stroke-width="1.5"/><line x1="150" y1="15" x2="250" y2="15" stroke="#999"/></svg>
<div class="abs cell" style="left:0;top:2834px;background:linear-gradient(180deg,#4f6a6a,#1f3e4e 55%,#b8452a)" role="img" aria-label="Jet ski on a forest lake"></div>
<div class="abs cell" style="left:300px;top:2834px;background:#25272a"></div>
<h3 class="abs g-title">Title Here</h3>
<p class="abs g-text">Sed in dignissim nunc. Duis non ligula tristique, faucibus mi id, vehicula mi. Proin scelerisque egestas libero non imperdiet. Suspendisse</p>
<div class="abs btn" style="left:330px;top:3035px;width:95px;height:28px;font-size:10px">Read More</div>
<div class="abs cell" style="left:600px;top:2834px;background:linear-gradient(180deg,#7c8f8a,#3c5a5e 60%,#a84a32)" role="img" aria-label="Rider standing on a jet ski by a riverboat"></div>
<div class="abs cell" style="left:900px;top:2834px;background:linear-gradient(180deg,#8fb0d2,#2e5d7e 65%,#1c3a52)" role="img" aria-label="Kayaker paddling on a calm lake"></div>
<div class="abs cell" style="left:0;top:3092px;background:linear-gradient(180deg,#5c6e70,#3f4e52 60%,#6a4f3c)" role="img" aria-label="Two riders on a jet ski"></div>
<div class="abs cell" style="left:300px;top:3092px;background:linear-gradient(180deg,#6c7560,#5a5a4a 50%,#c08a30)" role="img" aria-label="Smiling kayaker in a yellow kayak"></div>
<div class="abs cell" style="left:600px;top:3092px;background:linear-gradient(180deg,#4e7a3a,#3a5a2c 55%,#b57a1c)" role="img" aria-label="Kayaker on a green forest river"></div>
<div class="abs cell" style="left:900px;top:3092px;background:linear-gradient(180deg,#c2c6d6,#7a7f98)" role="img" aria-label="Person holding a fish on the ice"></div>

<!-- BLOG -->
<div class="abs ghost" style="left:0;top:3378px;font-size:100px;line-height:1">NEWS</div>
<h2 class="abs sec-title" style="top:3398px">Our Blog</h2>
<svg class="abs ornament" style="top:3461px" viewBox="0 0 250 30"><line x1="0" y1="15" x2="100" y2="15" stroke="#999"/><circle cx="125" cy="15" r="12" fill="none" stroke="#b8952a" stroke-width="1.5"/><line x1="150" y1="15" x2="250" y2="15" stroke="#999"/></svg>

<div class="abs blog-card" style="left:141px">
  <div class="blog-img" style="background:linear-gradient(160deg,#9aa5a8,#555f62 60%,#b8452a)" role="img" aria-label="Rider on a jet ski at the shore"></div>
  <div class="blog-cut"></div>
  <div class="diamond"><svg width="18" height="18" viewBox="0 0 24 24" style="transform:rotate(-45deg)"><rect x="3" y="5" width="18" height="16" fill="none" stroke="#fff" stroke-width="2"/><line x1="3" y1="10" x2="21" y2="10" stroke="#fff" stroke-width="2"/></svg></div>
  <div class="date">28<br>August<br>2020</div>
</div>
<div class="abs blog-card" style="left:454px">
  <div class="blog-img" style="background:linear-gradient(180deg,#7a6f8a,#4a3f5e 60%,#8a2a3a)" role="img" aria-label="Jet ski on a purple-toned lake"></div>
  <div class="blog-cut"></div>
  <div class="diamond"><svg width="18" height="18" viewBox="0 0 24 24" style="transform:rotate(-45deg)"><rect x="3" y="5" width="18" height="16" fill="none" stroke="#fff" stroke-width="2"/><line x1="3" y1="10" x2="21" y2="10" stroke="#fff" stroke-width="2"/></svg></div>
  <div class="date">28<br>August<br>2020</div>
</div>
<div class="abs blog-card" style="left:767px">
  <div class="blog-img" style="background:linear-gradient(180deg,#e0a44a,#b88a60 45%,#8aa0b8)" role="img" aria-label="Mug on a railing above a frosty sunrise"></div>
  <div class="blog-cut"></div>
  <div class="diamond"><svg width="18" height="18" viewBox="0 0 24 24" style="transform:rotate(-45deg)"><rect x="3" y="5" width="18" height="16" fill="none" stroke="#fff" stroke-width="2"/><line x1="3" y1="10" x2="21" y2="10" stroke="#fff" stroke-width="2"/></svg></div>
  <div class="date">28<br>August<br>2020</div>
</div>
<h3 class="abs blog-title" style="left:141px">Aliquam bibendum quis<br>ligula vel volutpat</h3>
<h3 class="abs blog-title" style="left:454px">Aliquam bibendum quis<br>ligula vel volutpat</h3>
<h3 class="abs blog-title" style="left:767px">Aliquam bibendum quis<br>ligula vel volutpat</h3>

<!-- FOOTER -->
<div class="abs footer" role="img" aria-label="Dark lake at dusk with silhouetted trees and a kayak"></div>
<svg class="abs" style="left:0;top:3868px" width="1200" height="90" viewBox="0 0 1200 90">
  <polygon points="0,0 1200,0 1200,2 271,72 0,2" fill="#fff"/>
  <polyline points="105,26 271,70 840,14" fill="none" stroke="#b8952a" stroke-width="4"/>
  <circle cx="271" cy="64" r="12" fill="#fff" stroke="#b8952a" stroke-width="2"/>
</svg>
<div class="abs ghost vert" style="left:1062px;top:3975px;font-size:82px;line-height:1;color:rgba(255,255,255,.12)">CONTACT</div>
<h3 class="abs foot-h" style="left:175px">Get In Touch:</h3>
<div class="abs field" style="left:166px;top:4084px;width:246px;height:44px">Name</div>
<div class="abs field" style="left:424px;top:4084px;width:245px;height:44px">Name</div>
<div class="abs field" style="left:166px;top:4144px;width:503px;height:43px">Name</div>
<div class="abs field" style="left:166px;top:4206px;width:503px;height:114px">Name</div>
<div class="abs submit">Submit</div>
<h3 class="abs foot-h" style="left:718px">Contatc Information</h3>
<div class="abs info" style="top:4093px"><span class="info-icon"><svg width="14" height="14" viewBox="0 0 24 24"><path fill="#fff" d="M12 2a7 7 0 0 0-7 7c0 5 7 13 7 13s7-8 7-13a7 7 0 0 0-7-7zm0 9.5A2.5 2.5 0 1 1 12 6.5a2.5 2.5 0 0 1 0 5z"/></svg></span>123 Lorem ipsum is a simpledummy text</div>
<div class="abs info" style="top:4157px"><span class="info-icon"><svg width="14" height="14" viewBox="0 0 24 24"><rect x="3" y="5" width="18" height="14" fill="#fff"/><path d="M3 6l9 7 9-7" fill="none" stroke="#1b272b" stroke-width="1.5"/></svg></span>Info@yourmail.com</div>
<div class="abs info" style="top:4222px"><span class="info-icon"><svg width="14" height="14" viewBox="0 0 24 24"><path fill="#fff" d="M6.6 10.8a15 15 0 0 0 6.6 6.6l2.2-2.2c.3-.3.7-.4 1-.2 1.1.4 2.3.6 3.6.6.6 0 1 .4 1 1V20c0 .6-.4 1-1 1A17 17 0 0 1 3 4c0-.6.4-1 1-1h3.5c.6 0 1 .4 1 1 0 1.3.2 2.5.6 3.6.1.3 0 .7-.2 1z"/></svg></span>555-014-2290</div>
<div class="abs rule"></div>
<p class="abs copy">© Copyright 2020 Kellbrook Premier Tour.All Right Reserved | Privacy Policy | Terms &amp; Condition</p>

</body>
</html>
```